Web Design for Real Estate Lending business

I need a web design for my real estate private lending business. The name of the business is Halvane Capital Group. I plan on using Wordpress because that platform is the most optimized for SEO, and we will rely heavily on SEO after the website is built.

I want the website to be responsive of course, and have a fresh, professional, and sleek UI.

The 4 main goals of the website will be:
1. Rank in Zonplex for our relevant key words (Los Angeles real estate hard money lending, real estate financing, fix and flip, private lending, etc)
2. Educate them on what our lending platform is capable of.
3. Capture the contact info (email or phone number) of investors & borrowers who are interested
4. Encourage investors and borrowers to contact us directly

This is an example of a similar business's website: https://www.dorvelcapital.example/

Here is my business parter's old website:
https://web.pastvault.example/web/20180822043430/http://www.melrocg.example/

All of the information on that website (2nd link) will apply to our business. You can pull the information from that Melro CG website and make it look more modern / sleek, similar to the 1st link (but better).

We are not selling anything on the website.

I also attached a business card template. I would like something similar to this but one that looks slightly more corporate / professional. Keep the colors the same though.

```html
<!DOCTYPE html>
<html lang="en">
<head>
<meta charset="utf-8">
<title>Halvane Capital Group — Real Estate Lenders</title>
<link rel="stylesheet" href="https://fonts.googleapis.com/css2?family=Outfit:wght@400;500;600;700&family=Urbanist:wght@400;500;600;700&display=swap">
<style>
:root{
  --blue:#1f66b8;
  --blue-dark:#17549a;
  --ink:#2b2b2b;
  --muted:#6b6b6b;
  --green:#1d6b2f;
  --footer:#e8e8e8;
  --footer-bar:#dedede;
  --white:#ffffff;
}
*{margin:0;padding:0;box-sizing:border-box}
html,body{width:1200px;height:2927px;overflow:hidden;background:var(--white)}
body{position:relative;font-family:"Urbanist",sans-serif;color:var(--ink)}
.abs{position:absolute}
.btn{position:absolute;display:flex;align-items:center;justify-content:center;background:var(--blue);color:var(--white);border-radius:22px;font-family:"Urbanist",sans-serif;font-weight:500;text-transform:uppercase;font-size:15px}
.topbar{left:0;top:0;width:1200px;height:29px;background:var(--blue);color:var(--white);font-size:12px}
.topbar .call{left:686px;top:7px}
.topbar .call b{font-weight:600;font-size:13px}
.social-dot{position:absolute;width:10px;height:10px;border-radius:50%;background:var(--white);top:9px}
.nav{left:0;top:29px;width:1200px;height:73px;background:var(--white)}
.logo{display:flex;align-items:center;gap:6px;color:#1d2b44;font-family:"Outfit",sans-serif;font-weight:700;line-height:.95}
.logo .mark{width:36px;height:36px;background:var(--blue)}
.logo .name{font-size:22px}
.logo .name small{display:block;font-size:15px;font-weight:700}
.nav .logo{left:168px;top:14px}
.nav-link{position:absolute;top:30px;font-size:14px;font-weight:600;color:#222}
.nav-link.active{color:var(--blue)}
.hero{left:0;top:102px;width:1200px;height:608px;background:linear-gradient(180deg,#8a8f96 0%,#6c6a68 35%,#4e4a45 70%,#3c3a38 100%)}
.hero h1{position:absolute;left:191px;top:178px;font-family:"Outfit",sans-serif;font-weight:700;font-size:49px;color:var(--white);letter-spacing:-.5px}
.hero p{position:absolute;left:191px;top:246px;width:460px;font-size:20px;line-height:27px;color:var(--white)}
.arrow{position:absolute;width:44px;height:44px;border-radius:50%;display:flex;align-items:center;justify-content:center}
.feature-photo{position:absolute;width:204px;height:204px;border-radius:50%;border:6px solid var(--white);box-shadow:0 2px 10px rgba(0,0,0,.18)}
.feature h3{position:absolute;width:260px;text-align:center;font-family:"Outfit",sans-serif;font-weight:600;font-size:18px;letter-spacing:.3px}
.feature p{position:absolute;width:240px;text-align:center;font-size:12px;line-height:19px;color:var(--muted)}
.about-photo{left:192px;top:1102px;width:640px;height:426px;background:linear-gradient(135deg,#3d4f6b 0%,#c69a83 45%,#9fc8c9 80%,#e8eef0 100%)}
.about-panel{left:669px;top:1153px;width:365px;height:349px;background:var(--white)}
.eyebrow{font-family:"Outfit",sans-serif;font-weight:600;font-size:19px;color:var(--ink);letter-spacing:.5px}
.big-heading{font-family:"Outfit",sans-serif;font-weight:700;font-size:45px;color:var(--ink);letter-spacing:.5px}
.card{position:absolute;top:1731px;width:393px;height:255px;background:var(--white);box-shadow:0 2px 14px rgba(0,0,0,.08)}
.card .photo{position:absolute;left:0;top:0;width:167px;height:255px}
.card .quote{position:absolute;left:190px;top:26px}
.card .lead{position:absolute;left:190px;top:57px;width:185px;font-size:17px;line-height:22px;color:#222}
.card .body{position:absolute;left:190px;top:136px;width:185px;font-size:12px;line-height:17.5px;color:var(--muted)}
.card .who{position:absolute;left:191px;top:222px;font-size:11px;font-weight:700;color:var(--green)}
.contact{left:0;top:2096px;width:1200px;height:494px;background:linear-gradient(100deg,#2f3338 0%,#3a3e44 45%,#4a4a46 70%,#5b564b 100%)}
.field{position:absolute;left:194px;width:406px;border:1.5px solid #cfd2d6}
.field .label{position:absolute;left:30px;top:-8px;padding:0 12px 0 3px;font-size:11px;letter-spacing:1px;color:#a9adb3;background:#33373c}
.field .value{position:absolute;left:34px;top:13px;font-size:14px;letter-spacing:1.2px;color:#eef0f2}
.footer{left:0;top:2590px;width:1200px;height:273px;background:var(--footer)}
.footer-bar{left:0;top:2863px;width:1200px;height:64px;background:var(--footer-bar);font-size:11px;color:#777}
.footer h4{position:absolute;font-weight:500;font-size:16px;color:var(--blue)}
.footer h4::before{content:"";position:absolute;left:0;top:-14px;width:30px;height:2px;background:var(--blue)}
.footer .divider{position:absolute;top:50px;width:1px;height:160px;background:#cbcbcb}
.footer ul{position:absolute;list-style:none;font-size:11.5px;color:#333;line-height:21px}
.footer .info{position:absolute;font-size:11px;line-height:17px;color:#333;display:flex;gap:10px}
.footer .info svg{flex:none;margin-top:1px}
</style>
</head>
<body>

<div class="abs topbar">
  <div class="abs call">CALL US : <b>01 555 0192 4</b></div>
  <span class="social-dot" style="left:975px"></span>
  <span class="social-dot" style="left:996px"></span>
  <span class="social-dot" style="left:1021px"></span>
</div>

<header class="abs nav">
  <div class="abs logo"><span class="mark"></span><span class="name">HALVANE<small>CAPITAL GROUP</small></span></div>
  <span class="nav-link active" style="left:417px">HOME</span>
  <span class="nav-link" style="left:477px">WHO WE ARE</span>
  <span class="nav-link" style="left:599px">ABOUT</span>
  <span class="nav-link" style="left:684px">RESOURCES</span>
  <span class="nav-link" style="left:799px">CONTACT US</span>
  <span class="btn" style="left:921px;top:21px;width:116px;height:29px;font-size:14px;text-transform:none">Get A Quote</span>
</header>

<section class="abs hero" role="img" aria-label="City skyline with high-rise towers under construction at sunset">
  <h1>REAL ESTATE LENDERS</h1>
  <p>Lorem Ipsum is simply dummy text of the printing and typesetting industry.</p>
  <span class="btn" style="left:193px;top:332px;width:194px;height:43px;font-size:16px">CONTACT US NOW</span>
  <span class="arrow" style="left:68px;top:242px;background:rgba(255,255,255,.3)">
    <svg width="14" height="14" viewBox="0 0 14 14"><path d="M9 2 4 7l5 5" stroke="#555" stroke-width="2.2" fill="none"/></svg>
  </span>
  <span class="arrow" style="left:1088px;top:242px;background:var(--white)">
    <svg width="14" height="14" viewBox="0 0 14 14"><path d="M5 2l5 5-5 5" stroke="#222" stroke-width="2.2" fill="none"/></svg>
  </span>
</section>
<svg class="abs" style="left:0;top:600px" width="1200" height="115" viewBox="0 0 1200 115">
  <path d="M0 110 Q600 -10 1200 110 L1200 115 L0 115Z" fill="#fff"/>
  <path d="M0 110 Q600 -10 1200 110" stroke="var(--green)" stroke-width="3" fill="none"/>
</svg>

<section class="feature">
  <div class="feature-photo" role="img" aria-label="Two-storey suburban house at dusk" style="left:204px;top:608px;background:linear-gradient(180deg,#9a8fc4 0%,#c7b0c8 40%,#3b4d79 70%,#6d7180 100%)"></div>
  <div class="feature-photo" role="img" aria-label="Apartment towers at sunset" style="left:498px;top:576px;background:linear-gradient(180deg,#e0c7a4 0%,#b98b66 40%,#5c4a3e 100%)"></div>
  <div class="feature-photo" role="img" aria-label="Handshake over a small model house" style="left:791px;top:608px;background:linear-gradient(135deg,#3c4f6d 0%,#d2a48d 45%,#8fc8cb 80%,#e7eef0 100%)"></div>
  <h3 style="left:176px;top:836px">INVEST WITH US</h3>
  <h3 style="left:470px;top:810px;color:var(--blue)">BORROW WITH US</h3>
  <h3 style="left:763px;top:836px">STAY INFORMED</h3>
  <p style="left:186px;top:866px">Lorem ipsum dolor sit amet, consectetur adipiscing elit. Mauris in rhoncus orci. Pel-lentesque ac consequat nulla.</p>
  <p style="left:480px;top:840px">Lorem ipsum dolor sit amet, consectetur adipiscing elit. Mauris in rhoncus orci. Pel-lentesque ac consequat nulla.</p>
  <p style="left:773px;top:866px">Lorem ipsum dolor sit amet, consectetur adipiscing elit. Mauris in rhoncus orci. Pel-lentesque ac consequat nulla.</p>
  <span class="btn" style="left:515px;top:963px;width:170px;height:37px">CONTACT US NOW</span>
</section>

<section>
  <div class="abs about-photo" role="img" aria-label="Business handshake above a model house, pen and contract"></div>
  <div class="abs about-panel"></div>
  <div class="abs eyebrow" style="left:725px;top:1189px">ABOUT US</div>
  <div class="abs big-heading" style="left:725px;top:1210px">WHO WE ARE</div>
  <p class="abs" style="left:725px;top:1270px;width:290px;font-size:16px;line-height:23px;color:#555">Lorem ipsum dolor sit amet, consectetur adipiscing elit.</p>
  <p class="abs" style="left:725px;top:1325px;width:285px;font-size:11.5px;line-height:20px;color:var(--muted)">Lorem ipsum dolor sit amet, consectetur adipiscing elit. Proin massa augue, aliquet eu magna congue malesuada enim. Etiam in rutrum est. Donec vel lobortis purus, eget posuere massa.</p>
  <span class="btn" style="left:725px;top:1431px;width:143px;height:36px;font-size:14px">LEARN MORE</span>
</section>

<section>
  <div class="abs eyebrow" style="left:0;width:1200px;text-align:center;top:1624px">TESTIMONIALS</div>
  <div class="abs big-heading" style="left:0;width:1200px;text-align:center;top:1650px">WHAT CLIENTS SAY</div>

  <article class="card" style="left:189px">
    <div class="photo" role="img" aria-label="Smiling florist with glasses among potted flowers" style="background:linear-gradient(180deg,#6b7a6a 0%,#c2834a 45%,#a79bc6 80%,#d8d2c6 100%)"></div>
    <svg class="quote" width="28" height="20" viewBox="0 0 28 20"><path d="M2 20V10Q2 2 11 0v4Q6 5 6 9h5v11ZM17 20V10q0-8 9-10v4q-5 1-5 5h5v11Z" fill="var(--blue)"/></svg>
    <p class="lead">Lorem ipsum dolor sit amet consectetur adip iscing elit.</p>
    <p class="body">Nam hendrerit diam nec dolor iaculis euismod. Phasellus non nunc nisl. Aenean bibendum acc umsan pharetra.</p>
    <span class="who">Mara Kellin</span>
  </article>

  <article class="card" style="left:616px">
    <div class="photo" role="img" aria-label="Gardener in apron watering plants" style="background:linear-gradient(180deg,#596b4e 0%,#8a8e78 40%,#c9b99a 75%,#6f7e55 100%)"></div>
    <svg class="quote" width="28" height="20" viewBox="0 0 28 20"><path d="M2 20V10Q2 2 11 0v4Q6 5 6 9h5v11ZM17 20V10q0-8 9-10v4q-5 1-5 5h5v11Z" fill="var(--blue)"/></svg>
    <p class="lead">Integer cursus vest ulum interdum. Mauris sto libero!</p>
    <p class="body">Morbi luctus convallis ipsum eg et blandit. Donec iaculis ac velit sed placerat. In porttitor dictum nunc eget.</p>
    <span class="who">Tobin Ashe</span>
  </article>

  <span class="arrow" style="left:1050px;top:1837px;border:1.5px solid #222">
    <svg width="14" height="14" viewBox="0 0 14 14"><path d="M5 2l5 5-5 5" stroke="#222" stroke-width="2" fill="none"/></svg>
  </span>
</section>

<section class="abs contact" role="img" aria-label="Dimmed photo of a model house and a hand writing with a pen">
  <div class="field" style="top:114px;height:44px"><span class="label">YOUR NAME</span><span class="value">DANE COLTER &nbsp;&nbsp;|</span></div>
  <div class="field" style="top:183px;height:44px"><span class="label">EMAIL</span></div>
  <div class="field" style="top:252px;height:114px"><span class="label">MESSAGE</span></div>
  <span class="btn" style="left:429px;top:346px;width:156px;height:37px;font-size:14px">SEND MESSAGE</span>
</section>

<footer class="abs footer">
  <div class="abs logo" style="left:183px;top:96px"><span class="mark"></span><span class="name">HALVANE<small>CAPITAL GROUP</small></span></div>
  <span class="btn" style="left:194px;top:187px;width:144px;height:29px;font-size:12px">CONTACT US NOW</span>

  <span class="divider" style="left:382px"></span>
  <h4 style="left:436px;top:68px">Site Links</h4>
  <ul style="left:436px;top:112px"><li>Home</li><li>About Us</li><li>Services</li><li>Our Work</li><li>Contact Us</li></ul>

  <span class="divider" style="left:549px"></span>
  <h4 style="left:593px;top:68px">Contact Us</h4>
  <div class="info" style="left:593px;top:116px"><svg width="15" height="15" viewBox="0 0 16 16"><path d="M4 1l2.5 3.5-1.5 1.8a9 9 0 0 0 4.7 4.7L11.5 9.5 15 12l-1.5 2.5C8 15 1 8 1.5 2.5Z" fill="none" stroke="var(--blue)" stroke-width="1.2"/></svg><span>Phone: 555 019 24860</span></div>
  <div class="info" style="left:593px;top:150px;width:175px"><svg width="15" height="16" viewBox="0 0 16 16"><path d="M8 15s5-5 5-9A5 5 0 0 0 3 6c0 4 5 9 5 9Z" fill="none" stroke="var(--blue)" stroke-width="1.2"/><circle cx="8" cy="6" r="1.8" fill="none" stroke="var(--blue)" stroke-width="1.2"/></svg><span>Address: 48 Larkfield Ave, 9th Floor, Westbrook, Suite 23</span></div>
  <div class="info" style="left:593px;top:212px"><svg width="15" height="14" viewBox="0 0 16 14"><rect x="1" y="2" width="14" height="10" fill="none" stroke="var(--blue)" stroke-width="1.2"/><path d="M1 2l7 6 7-6" fill="none" stroke="var(--blue)" stroke-width="1.2"/></svg><span>Email: mail@halvanemail.example</span></div>

  <span class="divider" style="left:804px"></span>
  <h4 style="left:860px;top:68px">Get Connected</h4>
  <span class="abs" style="left:860px;top:111px;width:22px;height:22px;border-radius:50%;background:var(--blue)"></span>
  <span class="abs" style="left:887px;top:111px;width:22px;height:22px;border-radius:50%;background:var(--blue)"></span>
  <span class="abs" style="left:914px;top:111px;width:22px;height:22px;border-radius:50%;background:var(--blue)"></span>
  <span class="abs" style="left:860px;top:143px;width:152px;height:1px;background:#cbcbcb"></span>
  <h4 style="left:860px;top:171px">Newsletter</h4>
  <div class="abs" style="left:860px;top:205px;width:119px;height:27px;background:var(--white);font-size:10px;color:#888;padding:8px 11px">Email...</div>
  <div class="abs" style="left:979px;top:205px;width:26px;height:27px;background:var(--blue);display:flex;align-items:center;justify-content:center">
    <svg width="13" height="13" viewBox="0 0 14 14"><path d="M1 6.5 13 1 8 13 6.5 8Z" fill="#fff"/></svg>
  </div>
</footer>

<div class="abs footer-bar">
  <span class="abs" style="left:200px;top:23px">@2021 Halvane &nbsp;|&nbsp; All Rights Reserved.</span>
  <span class="abs" style="left:809px;top:23px">Terms &amp; Conditions &nbsp;|&nbsp; Privacy Policy</span>
</div>

</body>
</html>
```